Lorvant Stationary and Branding Documents

Corporate Identity Branding stationary needed for IT Recruiting Firm.

I already have a Logo, business cards and website. I need to get designs completed for the remaining corporate identity documents.

The documentation should use similar colors as my website and business card. The designs should modern and clean.

http://lorvantsystems.example/

Target Market(s)

Information Technology Industry

Industry/Entity Type

Information Technology

Colors
3377b5
0255a3
fbee3e
f78f20
f37122
33a6d7
000000
0592cd

Requirements
Must have
• Letter Head
• Folder Design
• PowerPoint Design
• Invoice
• Envelope
Nice to have
• Proposal
• Flyer
• Brochure
Should not have
• Logo
• Business Cards
• Website

```html
<!DOCTYPE html>
<html lang="en">
<head>
<meta charset="utf-8">
<title>Lorvant Stationery Set</title>
<link href="https://fonts.googleapis.com/css2?family=Quicksand:wght@400;500&family=Open+Sans:wght@400;600;700&family=Cinzel&display=swap" rel="stylesheet">
<style>
:root{
  --brand-blue:#0255a3;
  --mid-blue:#1b7ac6;
  --env-blue:#0a5aa6;
  --env-line:#084f93;
  --orange:#f37122;
  --orange-light:#f78f20;
  --line-blue:#3377b5;
  --row-grey:#ececec;
  --text-grey:#555;
  --paper:#ffffff;
  --bg:#ffffff;
}
*{box-sizing:border-box;margin:0;padding:0}
html,body{width:1200px;height:1200px;overflow:hidden;background:var(--bg)}
body{position:relative;font-family:"Open Sans",sans-serif;color:var(--text-grey)}
.sheet{position:absolute;background:var(--paper);box-shadow:0 0 0 1px #e6e6e6}
.brand{position:absolute;line-height:1}
.brand-name{font-family:"Quicksand",sans-serif;font-weight:500;color:var(--brand-blue);display:block;letter-spacing:.5px}
.brand-sub{font-family:"Quicksand",sans-serif;font-weight:500;color:var(--orange);display:block;letter-spacing:1px;white-space:nowrap}
.rule{position:absolute;height:1px;background:var(--line-blue)}
.contact-addr,.contact-reach{position:absolute;text-align:right;line-height:1;white-space:nowrap;font-family:"Open Sans",sans-serif}
.contact-addr{color:var(--orange);font-weight:700}
.contact-reach{color:var(--text-grey);font-weight:400}
.site{position:absolute;font-weight:700;color:#333;white-space:nowrap;font-family:"Open Sans",sans-serif}

/* letterhead */
.letterhead{left:75px;top:33px;width:383px;height:540px}
.letterhead .brand{left:25px;top:27px}
.letterhead .brand-name{font-size:25px}
.letterhead .brand-sub{font-size:6.5px;margin-top:1px}
.letterhead .rule.top{left:137px;top:52px;width:202px}
.letterhead .contact-addr{right:44px;top:44px;font-size:6px}
.letterhead .contact-reach{right:44px;top:55px;font-size:5.5px}
.letterhead .rule.foot{left:25px;top:511px;width:314px}
.letterhead .site{left:25px;top:516px;font-size:5px}

/* invoice */
.invoice{left:516px;top:35px;width:415px;height:538px;font-family:"Quicksand",sans-serif}
.invoice .brand{left:38px;top:33px}
.invoice .brand-name{font-size:27px}
.invoice .brand-sub{font-size:7px;margin-top:1px}
.invoice .rule.top{left:158px;top:62px;width:218px}
.invoice .contact-addr{right:39px;top:54px;font-size:6px}
.invoice .contact-reach{right:39px;top:65px;font-size:5.5px}
.inv-title{position:absolute;left:39px;top:88px;font-size:17px;color:var(--orange);font-weight:400}
.inv-title b{font-weight:500}
.inv-dates{position:absolute;left:39px;top:111px;font-size:5.5px;line-height:1.6;color:#888}
.parties{position:absolute;left:38px;top:131px;width:338px;height:76px;border:1px solid var(--orange);display:flex}
.party{flex:1;padding:2px;position:relative}
.party+.party{border-left:1px solid var(--orange)}
.party-head{background:var(--brand-blue);color:#fff;font-size:8px;padding:5px 6px;height:20px}
.party-logo{position:absolute;left:6px;top:31px;width:38px;height:36px;border:1px solid #eee;display:flex;align-items:center;justify-content:center;font-size:6.5px;color:var(--brand-blue);font-weight:500}
.party-logo.empty{color:#ccc}
.party-lines{position:absolute;left:50px;right:3px;top:24px;font-size:4.5px;color:#666}
.party-lines div{background:var(--row-grey);height:8.5px;margin-bottom:1.1px;padding:1.5px 2px;line-height:1.2}
.items-label{position:absolute;left:41px;top:215px;font-size:7px;color:#555}
.items{position:absolute;left:38px;top:229px;width:338px;border-collapse:separate;border-spacing:0 3px;font-size:5px;color:#666}
.items thead th{background:var(--orange);color:#fff;font-weight:400;height:20px;text-align:left;padding:0 5px}
.items td{background:var(--row-grey);height:20px;padding:0 5px;border-right:2px solid #fff}
.items .num{text-align:center}
.items .money{text-align:right}
.notes{position:absolute;left:38px;top:408px;width:218px;height:66px;border:1px solid #e4e4e4;padding:10px 6px;font-size:5.5px;color:#555}
.notes i{display:block;height:1px;background:#eee;margin-top:10px}
.notes-foot{position:absolute;left:41px;top:480px;font-size:4.5px;color:#555;white-space:nowrap}
.amount{position:absolute;left:271px;top:403px;width:104px;border:1px solid #e4e4e4;font-size:5px;color:#666}
.amount-head{background:var(--brand-blue);color:#fff;font-size:8px;text-align:center;height:20px;line-height:20px}
.amount-row{display:flex;justify-content:space-between;padding:0 6px 0 12px;height:16.5px;align-items:center;border-bottom:1px solid #eee}
.amount-row.total{height:18px;justify-content:flex-end;gap:3px;border-bottom:0}
.amount-row.total span:last-child{font-size:10px;color:var(--brand-blue)}
.invoice .rule.foot{left:41px;top:509px;width:334px}
.invoice .site{left:41px;top:514px;font-size:5px}

/* folder */
.folder{left:73px;top:595px;width:433px;height:576px;background:var(--mid-blue);overflow:hidden}
.folder-photo{position:absolute;left:0;top:0;width:433px;height:300px;background:linear-gradient(135deg,#7fc3e6,#dbeef8 55%,#c9d7e2)}
.folder .brand{left:0;right:0;top:418px;text-align:center}
.folder .brand-name{font-size:50px;color:#fff;letter-spacing:2px}
.folder .brand-sub{font-size:13px;margin-top:4px;letter-spacing:2px}
.folder .brand-sub::before,.folder .brand-sub::after{content:"";display:inline-block;width:6px;height:2px;background:var(--orange);vertical-align:middle;margin:0 12px}
.tagline{position:absolute;left:0;right:0;top:505px;height:20px;background:linear-gradient(var(--orange-light),var(--orange));color:#fff;font-family:"Cinzel",serif;font-size:14px;text-align:center;line-height:20px;letter-spacing:1px}
.folder-foot{position:absolute;left:0;right:0;top:565px;height:1.5px;background:#fff}
.folder-site{position:absolute;left:162px;top:558px;padding:2px 9px;background:var(--brand-blue);border-radius:8px;color:#fff;font-size:8px;font-weight:600}

/* compliment slip */
.slip{left:550px;top:602px;width:584px;height:294px}
.slip .brand{left:27px;top:30px}
.slip .brand-name{font-size:36px}
.slip .brand-sub{font-size:9px;margin-top:2px;letter-spacing:1.5px}
.slip .rule.top{left:192px;top:66px;width:370px}
.slip .contact-addr{right:32px;top:56px;font-size:7px}
.slip .contact-reach{right:32px;top:70px;font-size:7px}
.slip .rule.foot{left:19px;top:268px;width:558px}
.slip .site{left:19px;top:274px;font-size:6.5px}

/* envelope */
.envelope{left:551px;top:910px;width:586px;height:275px;background:var(--env-blue)}
.envelope svg{position:absolute;left:0;top:0}
</style>
</head>
<body>

<section class="sheet letterhead" aria-label="Letterhead">
  <div class="brand"><span class="brand-name">Lorvant</span><span class="brand-sub">- BUSINESS SOLUTION LLC -</span></div>
  <div class="rule top"></div>
  <div class="contact-addr">Two Harbor Plaza 410, 9th Avenue</div>
  <div class="contact-reach">☎ 5550148270 ✉ info@lorvantsystems.example</div>
  <div class="rule foot"></div>
  <div class="site">www.lorvantsystems.example</div>
</section>

<section class="sheet invoice" aria-label="Invoice">
  <div class="brand"><span class="brand-name">Lorvant</span><span class="brand-sub">- BUSINESS SOLUTION LLC -</span></div>
  <div class="rule top"></div>
  <div class="contact-addr">Two Harbor Plaza 410, 9th Avenue</div>
  <div class="contact-reach">☎ 5550148270 ✉ info@lorvantsystems.example</div>
  <h1 class="inv-title">Invoice <b>0001</b></h1>
  <div class="inv-dates">01 September , 2012<br>Payment due by 25 November 2012</div>
  <div class="parties">
    <div class="party">
      <div class="party-head">FROM</div>
      <div class="party-logo">Lorvant</div>
      <div class="party-lines"><div>Your Address</div><div>Address Line 1</div><div>Town</div><div>Region/State</div><div>Zip/Postal Code</div></div>
    </div>
    <div class="party">
      <div class="party-head">TO</div>
      <div class="party-logo empty">LOGO</div>
      <div class="party-lines"><div>Your Address</div><div>Address Line 1</div><div>Town</div><div>Region/State</div><div>Zip/Postal Code</div></div>
    </div>
  </div>
  <div class="items-label">ITEMS</div>
  <table class="items">
    <colgroup><col style="width:44px"><col><col style="width:58px"><col style="width:68px"></colgroup>
    <thead><tr><th class="num">Quantity</th><th>Description</th><th class="money">Unit Price</th><th class="money">TOTAL</th></tr></thead>
    <tbody>
      <tr><td class="num">2</td><td>Donec ac erat vel neque molestie convallis.</td><td class="money">$600</td><td class="money">$1200</td></tr>
      <tr><td class="num">1</td><td>Sed eget risus ac lacus tempus sollicitudin in at magna.</td><td class="money">$300</td><td class="money">$300</td></tr>
      <tr><td class="num">3</td><td>Nunc auctor nisl vel lorem aliquet pellentesque.</td><td class="money">$800</td><td class="money">$2400</td></tr>
      <tr><td class="num">2</td><td>Pellentesque habitant morbi.</td><td class="money">$20</td><td class="money">$40</td></tr>
      <tr><td class="num">2</td><td>In hac habitasse platea dictumst mauris at.</td><td class="money">$2500</td><td class="money">$5000</td></tr>
      <tr><td class="num">1</td><td>Aenean eget enim eget augue dictum fringilla et vitae.</td><td class="money">$100</td><td class="money">$100</td></tr>
    </tbody>
  </table>
  <div class="notes">Special Notes<i></i><i></i></div>
  <div class="notes-foot">molestie condimentum. Curabitur mi dui, faucibus sed</div>
  <div class="amount">
    <div class="amount-head">AMOUNT DUE</div>
    <div class="amount-row"><span>SUBTOTAL</span><span>$9,040</span></div>
    <div class="amount-row"><span>TAX</span><span>$00.00</span></div>
    <div class="amount-row"><span>SHIPPING</span><span>$00.00</span></div>
    <div class="amount-row total"><span>TOTAL</span><span>$9,040.00</span></div>
  </div>
  <div class="rule foot"></div>
  <div class="site">www.lorvantsystems.example</div>
</section>

<section class="sheet folder" aria-label="Presentation folder">
  <div class="folder-photo" role="img" aria-label="Photo of a business team meeting around a laptop in a bright office, with a curved orange and grey accent below"></div>
  <div class="brand"><span class="brand-name">Lorvant</span><span class="brand-sub">BUSINESS SOLUTION LLC</span></div>
  <div class="tagline">JOIN THE ELITE</div>
  <div class="folder-foot"></div>
  <div class="folder-site">lorvantsystems.example</div>
</section>

<section class="sheet slip" aria-label="Compliment slip">
  <div class="brand"><span class="brand-name">Lorvant</span><span class="brand-sub">- BUSINESS SOLUTION LLC -</span></div>
  <div class="rule top"></div>
  <div class="contact-addr">Two Harbor Plaza 410, 9th Avenue</div>
  <div class="contact-reach">☎ 5550148270 ✉ info@lorvantsystems.example</div>
  <div class="rule foot"></div>
  <div class="site">www.lorvantsystems.example</div>
</section>

<section class="envelope sheet" aria-label="Envelope back">
  <svg width="586" height="275" viewBox="0 0 586 275">
    <path d="M8 8 L28 130 Q32 142 48 142 L538 142 Q554 142 558 130 L578 8" fill="none" stroke="#084f93" stroke-width="2"/>
    <path d="M0 275 L40 150 M586 275 L546 150" stroke="#084f93" stroke-width="1.5"/>
  </svg>
</section>

</body>
</html>
```